LSV AUDITION

I need a post card design (front only) with this on it:
Leap Spin Vibe (this is the main title to be in all caps)
Auditions
Date: Thursday June 30th
6:30-8:30 PM in person
Address: 4170 Wexley BLVD, Oakland CA 94611
video submissions turn in by Sunday July 3rd, 2022 email:LeapSpinVibe22@trovemail.net
Teens and Adults welcomed

SO PLEASE COME UP WITH A DESIGN THATS COLORFUL AND INVITING THX!

```html
<!DOCTYPE html>
<html lang="en">
<head>
<meta charset="utf-8">
<title>Leap Spin Vibe Auditions Postcard</title>
<link href="https://fonts.googleapis.com/css2?family=Playfair+Display:wght@700;800&family=Sacramento&family=Alegreya+Sans:wght@400;700&display=swap" rel="stylesheet">
<style>
  :root {
    --backdrop: #9a9a9a;
    --hero-rose: #e03a5c;
    --hero-magenta: #b0245f;
    --hero-plum: #781670;
    --hero-coral: #c9474f;
    --title-white: #ffffff;
    --title-shadow: #161010;
    --script-yellow: #f5e01e;
    --info-bg: #ffffff;
    --ink: #2a2a2a;
  }
  * { margin: 0; padding: 0; box-sizing: border-box; }
  html, body {
    width: 1200px; height: 893px; overflow: hidden;
    background: var(--backdrop);
  }
  .postcard {
    position: absolute; left: 60px; top: 93px;
    width: 1080px; height: 720px;
    background: var(--info-bg);
    overflow: hidden;
  }
  .hero {
    position: absolute; left: 0; top: 0; width: 1080px; height: 545px;
    background: linear-gradient(100deg, var(--hero-rose) 0%, var(--hero-magenta) 28%, var(--hero-plum) 52%, #9c2c6a 66%, var(--hero-coral) 100%);
  }
  .hero-photo {
    position: absolute; left: 560px; top: 0; width: 520px; height: 545px;
    background:
      radial-gradient(ellipse at 62% 55%, rgba(240,120,150,0.55) 0%, rgba(240,120,150,0) 60%),
      linear-gradient(90deg, rgba(156,44,106,0) 0%, rgba(205,76,84,0.6) 40%, rgba(205,76,84,0.85) 100%);
  }
  .title {
    position: absolute; left: 66px; top: 32px;
    font-family: "Playfair Display", serif; font-weight: 800;
    font-size: 118px; line-height: 122px; letter-spacing: 1px;
    color: var(--title-white);
    text-shadow: -3px 3px 0 var(--title-shadow);
    text-transform: uppercase;
  }
  .title span { display: block; }
  .subtitle {
    position: absolute; left: 66px; top: 386px;
    font-family: "Sacramento", cursive;
    font-size: 122px; line-height: 1;
    color: var(--script-yellow);
  }
  .info {
    position: absolute; left: 0; top: 545px; width: 1080px; height: 175px;
    font-family: "Alegreya Sans", sans-serif; color: var(--ink);
    font-size: 17.5px; line-height: 24px; letter-spacing: 0.4px;
  }
  .info b { font-weight: 700; }
  .info-col { position: absolute; }
  .info-when { left: 68px; top: 42px; }
  .info-video { left: 400px; top: 50px; }
  .info-who {
    left: 760px; width: 320px; top: 57px; text-align: center;
    font-size: 29px; line-height: 34px; font-weight: 700; letter-spacing: 0.3px;
  }
  .divider { position: absolute; top: 40px; }
  .divider-a { left: 362px; }
  .divider-b { left: 749px; }
</style>
</head>
<body>
  <main class="postcard">
    <section class="hero">
      <div class="hero-photo" role="img" aria-label="Photo of two dancers in colourful neon light striking a dance pose"></div>
      <h1 class="title"><span>Leap</span><span>Spin</span><span>Vibe</span></h1>
      <p class="subtitle">Auditions</p>
    </section>
    <section class="info">
      <div class="info-col info-when">
        <b>Time:</b> 6:30-8:30 PM in person<br>
        <b>Date:</b> Thursday June 30th<br>
        <b>Address:</b> 4170 Wexley BLVD,<br>
        Oakland CA 94611
      </div>
      <svg class="divider divider-a" width="12" height="100" viewBox="0 0 12 100" aria-hidden="true">
        <line x1="4" y1="0" x2="4" y2="100" stroke="#2a2a2a" stroke-width="2"/>
        <polygon points="4,44 12,50 4,56" fill="#2a2a2a"/>
      </svg>
      <div class="info-col info-video">
        Video submissions turn in by<br>
        <b>Sunday July 3rd, 2022</b><br>
        <b>Email:</b> LeapSpinVibe22@trovemail.net
      </div>
      <svg class="divider divider-b" width="12" height="100" viewBox="0 0 12 100" aria-hidden="true">
        <line x1="4" y1="0" x2="4" y2="100" stroke="#2a2a2a" stroke-width="2"/>
        <polygon points="4,44 12,50 4,56" fill="#2a2a2a"/>
      </svg>
      <div class="info-col info-who">Teens and Adults<br>welcomed</div>
    </section>
  </main>
</body>
</html>
```